Business Cards, Letterhead, Envelopes etc.
Need design that fits with tech saavy customers
Business Cards, Letterhead, Envelopes etc.  -
Creative Brief
Use specific fonts
Use same font or one that works with the logo
Cutting-Edge
Mark T. Derrow
President
418 Welland Avenue Palo Alto, CA 94306
mark@derfinco.com
derfinco.com
CA DRE: #00461738, NMLS: #517264
Need design for business cards, letterhead, #10 envelopes and mailing labels for package shipments.

```html
<!DOCTYPE html>
<html lang="en">
<head>
<meta charset="utf-8">
<title>Derfinco Stationery</title>
<link href="https://fonts.googleapis.com/css2?family=Montserrat:wght@600;700&family=Open+Sans:wght@400;600;700&display=swap" rel="stylesheet">
<style>
:root{
  --stage:#b3b3b3;
  --paper:#ffffff;
  --brand-blue:#2b5fb4;
  --brand-green:#5aa832;
  --ink:#2b2b2b;
  --muted:#6a6a6a;
  --shadow:rgba(0,0,0,.25);
}
*{box-sizing:border-box;margin:0;padding:0}
html,body{width:1200px;height:626px;overflow:hidden}
body{background:var(--stage);font-family:"Open Sans",Arial,sans-serif;color:var(--ink);position:relative}
.sheet{position:absolute;background:var(--paper);box-shadow:0 1px 4px var(--shadow);overflow:hidden}
.wordmark{font-family:"Montserrat",Arial,sans-serif;font-weight:700;color:var(--brand-blue);letter-spacing:.5px;display:flex;align-items:center;gap:5px;white-space:nowrap;flex:none;line-height:1}
.wordmark .dot{display:inline-block;background:var(--brand-green);flex:none}
.masthead{position:absolute;left:0;right:0;display:flex;align-items:center}
.band{background:var(--brand-blue);flex:none}
.band-fill{flex:1 1 auto}

/* business card */
.card{left:29px;top:306px;width:136px;height:150px}
.card .wordmark{position:absolute;left:12px;top:16px;font-size:13px}
.card .wordmark .dot{width:7px;height:7px}
.card .card-band{position:absolute;left:0;right:0;top:44px;height:5px;background:var(--brand-blue)}
.card .contact{position:absolute;left:0;right:0;top:66px;text-align:center;font-size:5px;line-height:7.5px;color:var(--muted)}
.card .contact .name{font-size:7px;font-weight:700;color:var(--ink);line-height:9px}
.card .contact .role{font-size:5.5px;margin-bottom:3px}

/* letterhead */
.letter{left:240px;top:17px;width:344px;height:600px}
.letter .masthead{top:32px;gap:14px}
.letter .band{height:12px}
.letter .band-left{width:96px}
.letter .wordmark{font-size:20px}
.letter .wordmark .dot{width:9px;height:9px}
.letter .body{position:absolute;left:34px;right:34px;top:78px;font-size:7.5px;line-height:12.5px}
.letter .recipient{font-weight:700;margin-bottom:12px}
.letter .body p{margin-bottom:13px}
.letter .signature{width:110px;height:42px;margin:4px 0 2px;background:linear-gradient(90deg,#d9d9d9,#efefef)}
.letter .footer{position:absolute;left:0;right:0;bottom:12px;text-align:center;font-size:4.8px;color:var(--muted)}

/* envelope back */
.env-back{left:612px;top:38px;width:570px;height:270px}
.env-back svg{position:absolute;left:0;top:0}

/* envelope front */
.env-front{left:612px;top:348px;width:570px;height:262px}
.env-front .masthead{top:32px;gap:18px}
.env-front .band{height:16px}
.env-front .band-left{width:190px}
.env-front .wordmark{font-size:24px}
.env-front .wordmark .dot{width:11px;height:11px}
.env-front .return{position:absolute;left:0;right:0;bottom:22px;text-align:center;font-size:5px;color:var(--muted)}
</style>
</head>
<body>

<section class="sheet card" aria-label="Business card">
  <div class="wordmark"><span class="dot"></span>DERFINCO</div>
  <div class="card-band"></div>
  <div class="contact">
    <div class="name">Mark T. Derrow</div>
    <div class="role">President</div>
    <div>418 Welland Avenue Palo Alto, CA 94306</div>
    <div>mark@derfinco.com</div>
    <div>derfinco.com</div>
    <div>CA DRE: #00461738, NMLS: #517264</div>
  </div>
</section>

<section class="sheet letter" aria-label="Letterhead">
  <div class="masthead">
    <div class="band band-left"></div>
    <div class="wordmark"><span class="dot"></span>DERFINCO</div>
    <div class="band band-fill"></div>
  </div>
  <div class="body">
    <div class="recipient">Dana Wells<br>Client Services<br>Palo Alto office</div>
    <p>Thank you for choosing our team to guide your home loan. We review every detail so your closing stays calm, clear and on time, from the first call to the final signature.</p>
    <p>Our advisors compare rates from many lenders and explain each option in plain terms. You will always know the next step, the current rate and the costs involved before you sign anything.</p>
    <p>We also track market changes each week. If a better rate appears while your file is open, we will contact you right away and explain whether a change makes sense for your plans.</p>
    <p>Please send your recent statements, pay stubs and tax returns when convenient. We will prepare a full summary within two business days and share it with you by email.</p>
    <p>Thank you again for your trust. We look forward to working with you.</p>
    <div>Sincerely yours,</div>
    <div class="signature" role="img" aria-label="Handwritten signature"></div>
    <div>Mark T. Derrow<br>President</div>
  </div>
  <div class="footer">418 Welland Avenue Palo Alto, CA 94306 · mark@derfinco.com · derfinco.com · CA DRE: #00461738, NMLS: #517264</div>
</section>

<section class="sheet env-back" aria-label="Envelope back">
  <svg width="570" height="270" viewBox="0 0 570 270" aria-hidden="true">
    <path d="M0 0 H570 V52 H430 Q418 52 416 64 L414 72 Q412 84 400 84 H170 Q158 84 156 72 L154 64 Q152 52 140 52 H0 Z" fill="var(--brand-blue)"/>
  </svg>
</section>

<section class="sheet env-front" aria-label="Envelope front">
  <div class="masthead">
    <div class="band band-left"></div>
    <div class="wordmark"><span class="dot"></span>DERFINCO</div>
    <div class="band band-fill"></div>
  </div>
  <div class="return">418 Welland Avenue Palo Alto, CA 94306 · mark@derfinco.com · derfinco.com · CA DRE: #00461738, NMLS: #517264</div>
</section>

</body>
</html>
```